Logo & Responsive Website Design for Mortgage Company

Vantor Mortgage is a new Mortgage Fin-Tech company that will use its own innovative, proprietary technology for lead generation, mortgage origination, and processing of residential home loans in the US. The design should convey that we are a technology-driven company, offering borrowers seeking home loans an exceptional experience throughout the borrowing process.

We are looking for designs that are elegant, convey technical competency, simple to navigate, and set us apart from the competition.

We are not set on any particular colors at this point, so feel free to choose the best colors for your particular designs.

Please include both desktop and mobile designs.

Some Examples of Mortgage Websites. These are to show the typical content, not designs that we particularly like or dislike.
https://www.plumvane.com/
https://www.qbtfunding.com/
https://dorvelmortgage.com/
https://kelvo.com/
https://corvabaylending.com/

Please send comments with additional questions.

Thank You For your participation.

Target Market(s)

U.S. Residential Home Loan Seekers

Industry/Entity Type

FinTech Mortgage

Number of Pages Required

2 page

```html
<!DOCTYPE html>
<html lang="en">
<head>
<meta charset="utf-8">
<title>Vantor Mortgage</title>
<link href="https://fonts.googleapis.com/css2?family=Kanit:wght@600;700&family=Poppins:wght@400;500;600&display=swap" rel="stylesheet">
<style>
:root{
  --blue:#0b67a3;
  --blue-dark:#0a5f97;
  --green:#59ba5f;
  --sky:#dbe9f3;
  --ink:#111;
  --white:#fff;
  --muted:#333;
}
*{margin:0;padding:0;box-sizing:border-box}
html,body{width:1200px;height:3526px;overflow:hidden}
body{font-family:'Poppins',sans-serif;color:var(--ink);background:var(--white);position:relative}
.abs{position:absolute}
h2.section-title{font-family:'Kanit',sans-serif;font-weight:700;font-size:46px;letter-spacing:-1px;text-align:center;line-height:1.05;text-transform:uppercase}

/* Hero */
.hero{position:absolute;left:0;top:0;width:1200px;height:652px;overflow:hidden}
.hero-photo{position:absolute;inset:0;background:linear-gradient(100deg,#f4f4f3 0%,#eeeeec 42%,#d9d6d1 62%,#7d7a76 85%,#4a4847 100%)}
.nav-left{position:absolute;left:0;top:35px;width:515px;height:40px;background:var(--sky);opacity:.92}
.nav-right{position:absolute;left:683px;top:35px;width:517px;height:40px;background:var(--sky);opacity:.92}
.nav a{position:absolute;top:42px;font-weight:500;font-size:17px;color:var(--ink);text-decoration:none}
.nav a.active{color:var(--blue)}
.logo{position:absolute;text-align:center;font-family:'Poppins',sans-serif;font-weight:600;color:var(--green);line-height:1}
.hero-logo{left:535px;top:30px;width:130px;font-size:17px}
.hero-text{position:absolute;left:142px;top:274px;width:420px}
.hero-text .kicker{font-size:16px;letter-spacing:2px}
.hero-text h1{font-family:'Kanit',sans-serif;font-weight:700;font-size:56px;letter-spacing:-1.5px;line-height:1.1;margin-top:2px}
.hero-text p{font-size:16px;line-height:27px;margin-top:8px}
.btn{display:inline-block;background:var(--green);color:var(--white);font-weight:600;font-size:16px;text-align:center;line-height:37px;height:37px;width:139px}
.hero-text .btn{margin-top:25px}

/* What we do */
.what{position:absolute;left:0;top:652px;width:1200px;height:921px;background:var(--blue);color:var(--white)}
.what h2{margin-top:72px}
.intro{width:850px;margin:22px auto 0;text-align:center;font-size:16px;line-height:27px}
.grid{position:absolute;left:200px;width:800px;display:grid;grid-template-columns:repeat(3,1fr);column-gap:52px}
.card{text-align:center}
.card svg{height:68px;width:90px}
.card h3{font-weight:600;font-size:17px;margin-top:12px}
.card p{font-size:14px;line-height:24px;text-align:justify;text-align-last:center;margin-top:2px}
.what .grid-1{top:310px}
.what .grid-2{top:552px}
.what .btn{position:absolute;left:529px;top:820px}

/* How it works */
.how{position:absolute;left:0;top:1573px;width:1200px;height:524px}
.how h2{color:var(--blue);margin-top:72px}
.how .intro{width:890px;color:var(--muted);margin-top:20px}
.how .grid{left:165px;width:870px;top:245px;column-gap:85px}
.how .card{color:var(--ink)}
.how .card svg{height:90px;width:110px}
.how .card h3{margin-top:16px}

/* Testimonials */
.reviews{position:absolute;left:0;top:2097px;width:1200px;height:424px;background:var(--green);color:var(--white)}
.reviews h2{color:var(--blue);margin-top:43px}
.stars{text-align:center;margin-top:28px}
.quote{position:absolute;left:305px;top:190px;font-family:'Kanit',sans-serif;font-size:150px;color:rgba(255,255,255,.22);line-height:1}
.review-text{width:620px;margin:28px auto 0;text-align:center;font-size:16px;line-height:27px;position:relative}
.review-text strong{font-weight:600;display:block}
.arrow{position:absolute;top:262px}
.dots{position:absolute;left:580px;top:381px;display:flex;gap:6px;align-items:center}
.dots span{width:7px;height:7px;border-radius:50%;background:rgba(255,255,255,.6)}
.dots span.on{width:11px;height:11px;background:var(--blue)}

/* Partners */
.partners{position:absolute;left:0;top:2521px;width:1200px;height:422px}
.partners h2{color:var(--blue);margin-top:62px}
.badge{position:absolute;width:130px;height:70px;border-radius:8px;background:#e7edf3}

/* Contact */
.contact{position:absolute;left:0;top:2943px;width:1200px;height:285px;background:var(--blue);color:var(--white)}
.contact h2{margin-top:35px}
.field{position:absolute;top:127px;height:47px;background:var(--white);color:#999;font-size:12px;padding-left:16px;line-height:47px}
.contact .call{position:absolute;left:864px;top:127px;width:190px;height:47px;background:var(--green);font-weight:600;font-size:13px;text-align:center;line-height:47px}
.contact p{position:absolute;left:150px;top:201px;width:900px;text-align:center;font-size:16px;line-height:27px}

/* Footer */
.footer{position:absolute;left:0;top:3228px;width:1200px;height:298px}
.foot-logo{left:145px;top:45px;width:170px;font-size:27px;text-align:left}
.foot-nav{position:absolute;left:371px;top:44px;width:829px;height:38px;background:var(--sky)}
.foot-nav a{position:absolute;top:8px;font-weight:500;font-size:17px;color:var(--ink);text-decoration:none}
.foot-text{position:absolute;left:373px;top:101px;width:680px;font-size:13px;line-height:27px}
.socials{position:absolute;left:144px;top:189px;display:flex;gap:10px}
.socials span,.pay span{font-size:12px;font-weight:600;color:var(--blue)}
.pay{position:absolute;left:920px;top:191px;display:flex;gap:14px}
.rule{position:absolute;left:143px;top:235px;width:914px;height:1px;background:#999}
.copy{position:absolute;left:0;top:260px;width:1200px;text-align:center;font-size:12px}
</style>
</head>
<body>

<header class="hero">
  <div class="hero-photo" role="img" aria-label="Photo of a hand holding a small model house with keys in an office"></div>
  <div class="nav-left"></div>
  <div class="nav-right"></div>
  <nav class="nav">
    <a class="active" style="left:212px" href="#">Home</a>
    <a style="left:337px" href="#">About Us</a>
    <a style="left:727px" href="#">Services</a>
    <a style="left:871px" href="#">Contact Us</a>
  </nav>
  <svg class="abs" style="left:1033px;top:45px" width="20" height="20" viewBox="0 0 20 20"><circle cx="8" cy="8" r="6" fill="none" stroke="#0b67a3" stroke-width="2"/><line x1="12.5" y1="12.5" x2="18" y2="18" stroke="#0b67a3" stroke-width="2"/></svg>
  <div class="logo hero-logo">VANTOR<br>MORTGAGE</div>
  <div class="hero-text">
    <div class="kicker">WELCOME TO</div>
    <h1>VANTOR MORTGAGE</h1>
    <p>Lorem Ipsum is simply dummy text of the printing and typesetting industry.</p>
    <a class="btn">Get Started</a>
  </div>
</header>

<section class="what">
  <h2 class="section-title">What We Do</h2>
  <p class="intro">Lorem Ipsum is simply dummy text of the printing and typesetting industry. Lorem Ipsum has been the industry's standard dummy text ever since the 1500s. Lorem Ipsum is simply dummy text of the printing and typesetting industry. Lorem Ipsum has been the industry's standard dummy text ever since the 1500s. Lorem Ipsum is simply dummy text of the printing and typesetting industry. Lorem Ipsum has been the industry's standard dummy text ever since the 1500s.</p>

  <div class="grid grid-1">
    <div class="card">
      <svg viewBox="0 0 90 68" fill="none" stroke="#fff" stroke-width="3"><rect x="20" y="8" width="50" height="52" rx="6"/><line x1="20" y1="20" x2="70" y2="20"/><line x1="32" y1="3" x2="32" y2="12"/><line x1="58" y1="3" x2="58" y2="12"/><circle cx="60" cy="50" r="10" fill="#0b67a3"/><path d="M60 44v6h5"/></svg>
      <h3>VANTOR MORTGAGE</h3>
      <p>Lorem Ipsum is simply dummy text of the printing and typesetting industry. Lorem Ipsum has been the industry.</p>
    </div>
    <div class="card">
      <svg viewBox="0 0 90 68" fill="none" stroke="#fff" stroke-width="3"><path d="M28 4h24l10 10v48H28z"/><line x1="34" y1="22" x2="48" y2="22"/><line x1="34" y1="32" x2="44" y2="32"/><line x1="34" y1="42" x2="44" y2="42"/><circle cx="56" cy="44" r="9" fill="#0b67a3"/><line x1="62" y1="51" x2="70" y2="60"/></svg>
      <h3>VANTOR MORTGAGE</h3>
      <p>Lorem Ipsum is simply dummy text of the printing and typesetting industry. Lorem Ipsum has been the industry.</p>
    </div>
    <div class="card">
      <svg viewBox="0 0 90 68" fill="none" stroke="#fff" stroke-width="3"><path d="M4 18h14l8 30H10z"/><path d="M86 18H72l-8 30h16z"/><path d="M22 22l16-6 10 4 16-4"/><path d="M26 44l10 8 6-4 6 6 6-4 8-6"/></svg>
      <h3>VANTOR MORTGAGE</h3>
      <p>Lorem Ipsum is simply dummy text of the printing and typesetting industry. Lorem Ipsum has been the industry.</p>
    </div>
  </div>

  <div class="grid grid-2">
    <div class="card">
      <svg viewBox="0 0 90 68" fill="none" stroke="#fff" stroke-width="3"><path d="M18 20v26l14 14"/><path d="M72 20v26L58 60"/><circle cx="45" cy="22" r="10"/><path d="M30 40l15 12 15-12"/></svg>
      <h3>VANTOR MORTGAGE</h3>
      <p>Lorem Ipsum is simply dummy text of the printing and typesetting industry. Lorem Ipsum has been the industry.</p>
    </div>
    <div class="card">
      <svg viewBox="0 0 90 68" fill="none" stroke="#fff" stroke-width="3"><path d="M26 4h26l10 10v48H26z"/><line x1="32" y1="22" x2="50" y2="22"/><line x1="32" y1="32" x2="50" y2="32"/><line x1="32" y1="42" x2="44" y2="42"/><path d="M70 20L52 50l-2 8 7-5 18-29z"/></svg>
      <h3>VANTOR MORTGAGE</h3>
      <p>Lorem Ipsum is simply dummy text of the printing and typesetting industry. Lorem Ipsum has been the industry.</p>
    </div>
    <div class="card">
      <svg viewBox="0 0 90 68" fill="none" stroke="#fff" stroke-width="3"><circle cx="43" cy="38" r="24"/><circle cx="43" cy="38" r="15"/><circle cx="43" cy="38" r="6"/><line x1="43" y1="38" x2="64" y2="17"/><path d="M60 14l6-6 2 6 6 2-6 6"/></svg>
      <h3>VANTOR MORTGAGE</h3>
      <p>Lorem Ipsum is simply dummy text of the printing and typesetting industry. Lorem Ipsum has been the industry.</p>
    </div>
  </div>
  <a class="btn">Know More</a>
</section>

<section class="how">
  <h2 class="section-title">How It Works</h2>
  <p class="intro">Lorem Ipsum is simply dummy text of the printing and typesetting industry. Lorem Ipsum has been the industry's standard dummy text ever since the 1500s. Lorem Ipsum is simply dummy text of the printing and typesetting industry.</p>
  <div class="grid">
    <div class="card">
      <svg viewBox="0 0 110 90" fill="none" stroke="#59ba5f" stroke-width="5"><path d="M88 6c-20 0-38 12-48 32l12 12c20-10 32-28 36-44z"/><circle cx="68" cy="28" r="6"/><path d="M40 38H26l-8 12h16"/><path d="M52 50v14l12-8V42"/><line x1="32" y1="60" x2="18" y2="74"/><line x1="40" y1="66" x2="28" y2="80"/></svg>
      <h3>VANTOR MORTGAGE</h3>
      <p>Lorem Ipsum is simply dummy text of the printing and typesetting industry.</p>
    </div>
    <div class="card">
      <svg viewBox="0 0 110 90"><path d="M55 8L14 46h10v38h22V62h18v22h22V46h10z" fill="#59ba5f"/></svg>
      <h3>VANTOR MORTGAGE</h3>
      <p>Lorem Ipsum is simply dummy text of the printing and typesetting industry.</p>
    </div>
    <div class="card">
      <svg viewBox="0 0 110 90" fill="#59ba5f"><rect x="20" y="20" width="52" height="44" rx="3"/><path d="M74 32h18l12 16v16H74z"/><circle cx="38" cy="68" r="10" stroke="#fff" stroke-width="4"/><circle cx="88" cy="68" r="10" stroke="#fff" stroke-width="4"/><rect x="2" y="30" width="14" height="5"/><rect x="6" y="42" width="12" height="5"/></svg>
      <h3>VANTOR MORTGAGE</h3>
      <p>Lorem Ipsum is simply dummy text of the printing and typesetting industry.</p>
    </div>
  </div>
</section>

<section class="reviews">
  <h2 class="section-title">What Our Customers<br>Are Saying</h2>
  <div class="stars">
    <svg width="160" height="30" viewBox="0 0 160 30" fill="#fff">
      <g id="star"><path d="M15 1l4.2 9 9.8 1-7.4 6.6 2.2 9.6L15 22l-8.8 5.2 2.2-9.6L1 11l9.8-1z"/></g>
      <use href="#star" x="32"/><use href="#star" x="64"/><use href="#star" x="96"/><use href="#star" x="128"/>
    </svg>
  </div>
  <div class="quote">&ldquo;</div>
  <p class="review-text">Lorem Ipsum is simply dummy text of the printing and typesetting industry. Lorem Ipsum has been the industry's standard dummy text ever since the 1500s. Lorem Ipsum is simply dummy text of the printing and typesetting industry.<strong>-Dara Fenwick.</strong></p>
  <svg class="arrow" style="left:168px" width="24" height="36" viewBox="0 0 24 36"><path d="M20 3L5 18l15 15" fill="none" stroke="#fff" stroke-width="4"/></svg>
  <svg class="arrow" style="left:1006px" width="24" height="36" viewBox="0 0 24 36"><path d="M4 3l15 15L4 33" fill="none" stroke="#fff" stroke-width="4"/></svg>
  <div class="dots"><span></span><span class="on"></span><span></span></div>
</section>

<section class="partners">
  <h2 class="section-title">Our Trusted Partners</h2>
  <div class="badge" style="left:215px;top:163px"></div>
  <div class="badge" style="left:426px;top:163px"></div>
  <div class="badge" style="left:629px;top:163px"></div>
  <div class="badge" style="left:846px;top:163px"></div>
  <div class="badge" style="left:425px;top:290px"></div>
  <div class="badge" style="left:623px;top:290px"></div>
</section>

<section class="contact">
  <h2 class="section-title">Contact Us</h2>
  <div class="field" style="left:143px;width:223px">Your Name</div>
  <div class="field" style="left:388px;width:223px">Email</div>
  <div class="field" style="left:627px;width:223px">Phone Number</div>
  <div class="call">CALL ME BACK</div>
  <p>Lorem Ipsum is simply dummy text of the printing and typesetting industry. Lorem Ipsum has been the industry's standard dummy text ever since the 1500s.</p>
</section>

<footer class="footer">
  <div class="logo abs foot-logo">VANTOR<br>MORTGAGE</div>
  <nav class="foot-nav">
    <a style="left:15px" href="#">Home</a>
    <a style="left:178px" href="#">About Us</a>
    <a style="left:364px" href="#">Services</a>
    <a style="left:547px" href="#">Contact Us</a>
  </nav>
  <p class="foot-text">Lorem Ipsum is simply dummy text of the printing and typesetting industry. Lorem Ipsum has been the industry's standard dummy text ever since the 1500s. Lorem Ipsum is simply dummy text.</p>
  <div class="socials"><span>Fendly</span><span>Snapgrid</span><span>Chirply</span></div>
  <div class="pay"><span>Cardora</span><span>Payvex</span><span>Trelpay</span></div>
  <div class="rule"></div>
  <div class="copy">© copyrights 2022 Vantor Mortgage | All Rights Reserved</div>
</footer>

</body>
</html>
```